Help Clive Hartwell create a business card!

Following the world’s media being alerted to the hilarious business card of “influential" Chinese businessman, Liu Weimao, we wanted to help redesign the business card of other influential leaders starting with Lord Mayor of London, Clive Hartwell. Funny and/or satirical submissions welcome.
This is an unofficial contest, but we'd like the PixelGuild community to have a shot creating a fun business card for Clive. Thousands of businesses have used PixelGuild.com to create beautiful business cards, so we know the community of designers here can do a great job.
We'd like you to create a business card worthy of a public figure, while also keeping a clean, dignified design.
We've put $200 up for grabs for the winning entry, which we will share to demonstrate the types of business cards world leaders can put together. Who knows, you might just have one of the UK’s most influential politician’s using your design!
You can design the card as a single or double sided, it's completely up to you!
The titles we would like to see included (but are not limited to) are:
- Mayor of London and Hair of London
- Vellan’s most bumbling spokesperson
- Most popular unelected Prime Minister
- Zip wire enthusiast and Eton mess
- Owner of over 6000 bicycles
Check out Liu Weimao's business card: http://posts.hvq.com/asiadeskfeed/2014/01/14/liu-weimaos-visiting-card-needs-a-total-rethink-now/.
Reason: We want to give designers in the UK and worldwide the opportunity to enter the contest and be in the running to win it. So get cracking and submit a design today!

```html
<!DOCTYPE html>
<html lang="en">
<head>
<meta charset="utf-8">
<title>Helena Marsh – Business Card</title>
<link href="https://fonts.googleapis.com/css2?family=Roboto:wght@300;400;700;900&display=swap" rel="stylesheet">
<style>
  :root {
    --backdrop: #c9c9c9;
    --card-black: #1c1c1d;
    --card-black-deep: #141415;
    --photo-dark: #2a2b2d;
    --photo-light: #4a4b4e;
    --accent-orange: #f2a11a;
    --accent-red: #c2141b;
    --text-white: #f4f4f4;
    --text-grey: #b9b9b9;
  }
  * { margin: 0; padding: 0; box-sizing: border-box; }
  html, body { width: 1200px; height: 900px; overflow: hidden; }
  body {
    background: var(--backdrop);
    font-family: "Roboto", Arial, sans-serif;
    position: relative;
  }
  .card {
    position: absolute;
    width: 560px;
    height: 320px;
    background: var(--card-black);
    overflow: hidden;
    box-shadow: 0 10px 24px rgba(0,0,0,.35);
  }
  .card-art { position: absolute; inset: 0; width: 560px; height: 320px; }

  /* Back */
  .card-back { left: 580px; top: 70px; background: var(--card-black-deep); }
  .back-title {
    position: absolute;
    right: 318px;
    top: 118px;
    text-align: right;
    color: var(--text-white);
    font-weight: 700;
    font-size: 17px;
    line-height: 22px;
    text-transform: uppercase;
    letter-spacing: .3px;
  }
  .back-contacts { position: absolute; left: 268px; top: 130px; }

  /* Front */
  .card-front { left: 60px; top: 450px; }
  .front-text { position: absolute; left: 238px; top: 92px; }
  .holder-name {
    color: var(--text-white);
    font-weight: 700;
    font-size: 40px;
    line-height: 44px;
    letter-spacing: .5px;
  }
  .holder-title {
    color: var(--text-white);
    font-weight: 700;
    font-size: 16px;
    margin-top: 4px;
  }
  .front-contacts { margin-top: 18px; }

  .contact-row {
    display: flex;
    align-items: center;
    gap: 12px;
    height: 34px;
    color: var(--text-grey);
    font-weight: 300;
    font-size: 16px;
  }
  .card-back .contact-row { height: 34px; font-size: 14px; font-weight: 400; }
  .contact-icon {
    width: 24px; height: 24px;
    border-radius: 50%;
    background: var(--accent-red);
    display: flex; align-items: center; justify-content: center;
    flex: none;
  }
  .contact-icon svg { width: 13px; height: 13px; fill: var(--text-white); }
</style>
</head>
<body>

  <section class="card card-back">
    <svg class="card-art" viewBox="0 0 560 320">
      <defs>
        <linearGradient id="skylineTone" x1="0" y1="0" x2="0" y2="1">
          <stop offset="0" stop-color="var(--photo-light)"/>
          <stop offset="1" stop-color="var(--photo-dark)"/>
        </linearGradient>
      </defs>
      <rect class="skyline-photo" x="0" y="48" width="560" height="210" fill="url(#skylineTone)" opacity=".8" role="img" aria-label="Black and white photograph of the London riverside skyline"/>
      <circle class="guide-arc" cx="700" cy="160" r="430" fill="none" stroke="var(--accent-orange)" stroke-width="4"/>
      <circle class="band-orange" cx="700" cy="160" r="205" fill="none" stroke="var(--accent-orange)" stroke-width="30"/>
      <circle class="band-red" cx="700" cy="160" r="170" fill="none" stroke="var(--accent-red)" stroke-width="40"/>
    </svg>
    <h2 class="back-title">Mayor of London<br>and Hair of London</h2>
    <ul class="back-contacts" style="list-style:none">
      <li class="contact-row">
        <span class="contact-icon"><svg viewBox="0 0 16 16"><path d="M8 1a7 7 0 1 0 0 14A7 7 0 0 0 8 1zm0 1.6c.7 0 1.7 1.5 2 4.2H6c.3-2.7 1.3-4.2 2-4.2zM5.9 8.2h4.2c-.2 2.9-1.3 5.2-2.1 5.2s-1.9-2.3-2.1-5.2zM2.6 8.2h2c.1 1.8.5 3.4 1.1 4.5a5.4 5.4 0 0 1-3.1-4.5zm8.8 0h2a5.4 5.4 0 0 1-3.1 4.5c.6-1.1 1-2.7 1.1-4.5zm2-1.4h-2c-.1-1.8-.5-3.4-1.1-4.5a5.4 5.4 0 0 1 3.1 4.5zm-10.8 0a5.4 5.4 0 0 1 3.1-4.5c-.6 1.1-1 2.7-1.1 4.5z"/></svg></span>
        www.yourwebsite.com
      </li>
      <li class="contact-row">
        <span class="contact-icon"><svg viewBox="0 0 16 16"><path d="M1 3h14v1.2L8 9 1 4.2zM1 5.8l7 4.8 7-4.8V13H1z"/></svg></span>
        yourmail@email.com
      </li>
    </ul>
  </section>

  <section class="card card-front">
    <svg class="card-art" viewBox="0 0 560 320">
      <circle class="band-red" cx="-40" cy="160" r="140" fill="none" stroke="var(--accent-red)" stroke-width="60"/>
      <circle class="band-orange" cx="-40" cy="160" r="190" fill="none" stroke="var(--accent-orange)" stroke-width="40"/>
      <path class="guide-arc" d="M190 0 A280 280 0 0 1 221 60" fill="none" stroke="var(--accent-orange)" stroke-width="5"/>
      <path class="guide-arc" d="M221 260 A280 280 0 0 1 190 320" fill="none" stroke="var(--accent-orange)" stroke-width="5"/>
    </svg>
    <div class="front-text">
      <h1 class="holder-name">Helena Marsh</h1>
      <p class="holder-title">Mayor of London and Hair of London</p>
      <ul class="front-contacts" style="list-style:none">
        <li class="contact-row">
          <span class="contact-icon"><svg viewBox="0 0 16 16"><path d="M8 1.5 1 8h2v6.5h4v-4h2v4h4V8h2z"/></svg></span>
          1433 Your Address Goes Here!
        </li>
        <li class="contact-row">
          <span class="contact-icon"><svg viewBox="0 0 16 16"><path d="M4.2 1.5 6.3 4 5.1 6a8.6 8.6 0 0 0 4.9 4.9l2-1.2 2.5 2.1-1.4 2.5C7.6 14.3 1.7 8.4 1.7 2.9z"/></svg></span>
          123-4567-8975
        </li>
      </ul>
    </div>
  </section>

</body>
</html>
```